Bun Rush Showdown - Team Eating Comp

Design a fun/ vibrant/ edgy/ funny/ eye catching poster for our upcoming hotdog eating challenge. We are a grundgy whiskey/ burger bar on the Sunshine Coast. We have previously done hotdog eating comps and this year will be a hybrid model. I have attached an old tshirt design, this time more pop art in the design.

Info for the poster :
- teams of 2
- can you finish 14 hotdogs between you in 10min?
- $35 to enter (refunded if you successfully complete the challenge)
- prize if you successfully complete challenge
- 29th July 2023
- 12pm-5pm
Come down to Rusty Pikes Waratah for the challenge - one day only!!

rustypikeswaratah.com

Target Market(s)

Sunshine Coast locals. Food Competitors.

Industry/Entity Type

Bar and Restaurant

Font styles to use
Other font styles liked:
• Veneer

Colors
FFF300
FFF600
FEFA6F
FFFEC7
FFFEE8
F0912C
F2A743
F7CA91
FBE8D2
FDF5EE
EE7325
F08F49
F5BC92
FAE3D3
FDF4ED
EB3D1F
EC4F4E
F09395
F8D3D4
FCEDEE

```html
<!DOCTYPE html>
<html lang="en">
<head>
<meta charset="utf-8">
<title>Bun Rush Showdown – Team Eating Challenge Poster</title>
<link rel="stylesheet" href="https://fonts.googleapis.com/css2?family=Bebas+Neue&family=Exo+2:wght@600;800&family=Lilita+One&display=swap">
<style>
  :root {
    --backdrop: #b9d8d9;
    --frame: #52708c;
    --cream: #f9f1e6;
    --navy: #343a5a;
    --red: #e3615f;
    --ink: #1e1e22;
  }
  * { margin: 0; padding: 0; box-sizing: border-box; }
  html, body { width: 1200px; height: 900px; overflow: hidden; background: var(--backdrop); }
  .canvas { position: relative; width: 1200px; height: 900px; }

  .poster {
    position: absolute; left: 300px; top: 10px;
    width: 600px; height: 880px;
    border: 10px solid var(--frame);
    background: var(--cream);
    color: var(--navy);
    text-align: center;
  }
  .poster > * { position: absolute; left: 0; width: 100%; }

  .hero-art { top: 25px; left: 17px; width: 542px; height: 398px; }

  .brand-name {
    top: 8px; left: auto; right: 26px; width: auto;
    font-family: "Bebas Neue", sans-serif;
    font-size: 40px; line-height: 0.92;
    color: var(--ink); text-align: center;
  }

  .invite {
    top: 446px;
    font-family: "Exo 2", sans-serif; font-weight: 600;
    font-size: 20px; line-height: 20px; letter-spacing: 0.1px;
    text-transform: uppercase;
  }
  .invite .accent { color: var(--red); font-weight: 800; }

  .teams {
    top: 493px;
    font-family: "Lilita One", sans-serif;
    font-size: 29px; line-height: 34px; letter-spacing: 0.5px;
  }

  .wave { left: 28px; width: 516px; height: 8px; }
  .wave--top { top: 532px; }
  .wave--bottom { top: 655px; }

  .headline {
    top: 549px;
    font-family: "Bebas Neue", sans-serif; font-weight: 400;
    font-size: 54px; line-height: 50px; letter-spacing: 0.5px;
  }
  .headline .accent { color: var(--red); }

  .entry {
    top: 672px; height: 50px;
    display: flex; justify-content: center; align-items: center; gap: 8px;
    font-family: "Bebas Neue", sans-serif;
  }
  .entry-price { font-size: 50px; line-height: 1; }
  .entry-note { font-size: 21px; line-height: 21px; text-align: left; }

  .prize-banner { top: 736px; left: 23px; width: 527px; height: 42px; }
  .prize-text {
    top: 736px;
    font-family: "Bebas Neue", sans-serif;
    font-size: 28px; line-height: 30px; color: var(--cream); letter-spacing: 0.3px;
  }

  .event-when {
    top: 787px; height: 40px;
    font-family: "Lilita One", sans-serif;
    font-size: 34px; line-height: 40px; color: var(--red);
    display: flex; justify-content: center; align-items: center; gap: 16px;
  }
  .event-when .divider { width: 2px; height: 28px; background: var(--navy); }

  .website {
    top: 831px;
    font-family: "Exo 2", sans-serif; font-weight: 600;
    font-size: 21px; line-height: 24px;
  }
</style>
</head>
<body>
<div class="canvas">
  <svg width="0" height="0" aria-hidden="true" style="position:absolute">
    <defs>
      <pattern id="wave-pattern" width="12" height="8" patternUnits="userSpaceOnUse">
        <path d="M0 4 Q3 0 6 4 T12 4" fill="none" stroke="#343a5a" stroke-width="1.3"/>
      </pattern>
      <linearGradient id="hotdog-tone" x1="0" y1="0" x2="1" y2="1">
        <stop offset="0" stop-color="#c8502c"/>
        <stop offset="0.45" stop-color="#f2a743"/>
        <stop offset="1" stop-color="#e8962c"/>
      </linearGradient>
    </defs>
  </svg>

  <article class="poster">
    <svg class="hero-art" viewBox="0 0 542 398" role="img" aria-label="Illustrated hotdog in a bun with ketchup and mustard">
      <ellipse cx="271" cy="199" rx="280" ry="118" transform="rotate(24 271 199)" fill="url(#hotdog-tone)"/>
    </svg>

    <div class="brand-name">RUSTY<br>PIKES</div>

    <p class="invite">Come down to <span class="accent">Rusty Pikes Waratah</span> for the<br><span class="accent">Challenge - one day only!!</span></p>

    <p class="teams">TEAMS OF 2</p>

    <svg class="wave wave--top" aria-hidden="true"><rect width="100%" height="8" fill="url(#wave-pattern)"/></svg>

    <h1 class="headline">CAN YOU FINISH <span class="accent">14 HOTDOGS</span><br>BETWEEN YOU IN <span class="accent">10MIN?</span></h1>

    <svg class="wave wave--bottom" aria-hidden="true"><rect width="100%" height="8" fill="url(#wave-pattern)"/></svg>

    <div class="entry">
      <span class="entry-price">$35 TO ENTER</span>
      <span class="entry-note">(REFUNDED IF YOU SUCCESSFULLY<br>COMPLETE THE CHALLENGE)</span>
    </div>

    <svg class="prize-banner" viewBox="0 0 527 42" aria-hidden="true">
      <polygon points="0,12 40,12 40,42 12,42 24,27" fill="#343a5a"/>
      <polygon points="527,12 487,12 487,42 515,42 503,27" fill="#343a5a"/>
      <rect x="30" y="0" width="467" height="36" fill="#343a5a"/>
    </svg>
    <p class="prize-text">PRIZE IF YOU SUCCESSFULLY COMPLETE CHALLENGE</p>

    <p class="event-when"><span>29TH JULY 2023</span><span class="divider"></span><span>12PM-5PM</span></p>

    <p class="website">rustypikeswaratah.com</p>
  </article>
</div>
</body>
</html>
```